Quarlwick Builders Business Cards

I want to use the logo and make an unique business card that shows the textured Logo with brick and builings. I want to be able to stand out when I pass out business cards.

```html
<!DOCTYPE html>
<html lang="en">
<head>
<meta charset="utf-8">
<title>Quarlwick Builders Business Cards</title>
<link rel="stylesheet" href="https://fonts.googleapis.com/css2?family=Exo+2:ital,wght@0,500;0,600;0,800;1,800&family=Saira+Condensed:wght@800&display=swap">
<style>
  :root {
    --stage: #323232;
    --brick: #d2492a;
    --brick-dark: #8f2c18;
    --card-black: #0b0b0b;
    --accent: #f0552a;
    --ink-light: #ffffff;
  }
  * { margin: 0; padding: 0; box-sizing: border-box; }
  html, body { width: 1200px; height: 780px; overflow: hidden; }
  body {
    background: var(--stage);
    font-family: "Exo 2", sans-serif;
    position: relative;
  }
  .card {
    position: absolute;
    width: 620px;
    height: 354px;
    border-radius: 26px;
    overflow: hidden;
    box-shadow: 0 14px 30px rgba(0,0,0,.45);
  }
  .card--front { left: 40px; top: 30px; }
  .card--back { left: 540px; top: 396px; background: var(--card-black); }

  .brick-wall {
    position: absolute; inset: 0;
    background: radial-gradient(ellipse at 50% 50%, #e35a35 0%, var(--brick) 55%, var(--brick-dark) 100%);
  }
  .brand {
    position: absolute;
    display: flex; align-items: center; gap: 12px;
    font-family: "Exo 2", sans-serif;
    font-weight: 800;
    text-transform: uppercase;
    color: var(--ink-light);
  }
  .brand__dot { border-radius: 50%; background: var(--ink-light); flex: none; }
  .brand__name { display: block; white-space: nowrap; line-height: 1.05; }
  .brand__line { display: block; }
  .card--front .brand {
    left: 50%; top: 50%; transform: translate(-50%, -50%);
    font-size: 40px; letter-spacing: 1px;
  }
  .card--front .brand__dot { width: 22px; height: 22px; }
  .card--back .brand {
    left: 40px; top: 92px; font-size: 30px; letter-spacing: .5px;
  }
  .card--back .brand__dot { width: 18px; height: 18px; }

  .back-art { position: absolute; inset: 0; }

  .contact {
    position: absolute;
    right: 30px; top: 100px;
    text-align: right;
    color: var(--ink-light);
  }
  .contact__name {
    font-family: "Saira Condensed", sans-serif;
    font-weight: 800; font-size: 34px; line-height: 1;
    color: var(--accent); text-transform: uppercase; letter-spacing: .5px;
  }
  .contact__title { font-weight: 600; font-size: 17px; margin: 4px 0 12px; }
  .contact__line {
    display: flex; justify-content: flex-end; align-items: center; gap: 8px;
    font-weight: 600; font-size: 16px; line-height: 24px;
  }
  .contact__icon { width: 14px; height: 14px; flex: none; }

  .services {
    position: absolute; left: 30px; right: 24px; bottom: 22px;
    text-align: right;
    font-weight: 800; font-style: italic; font-size: 15px;
    color: var(--ink-light); letter-spacing: .5px; white-space: nowrap;
  }
  .services__dot { color: var(--accent); margin: 0 6px; }
</style>
</head>
<body>

<section class="card card--front">
  <div class="brick-wall" role="img" aria-label="Textured red brick wall background"></div>
  <div class="brand"><span class="brand__dot"></span><span class="brand__name">Quarlwick Builders</span></div>
</section>

<section class="card card--back">
  <svg class="back-art" viewBox="0 0 620 354" width="620" height="354">
    <defs>
      <linearGradient id="wallTone" x1="0" y1="0" x2="1" y2="1">
        <stop offset="0" stop-color="#454545"/>
        <stop offset="1" stop-color="#1f1f1f"/>
      </linearGradient>
      <linearGradient id="silverBand" x1="0" y1="1" x2="1" y2="0">
        <stop offset="0" stop-color="#d9d9d9"/>
        <stop offset=".45" stop-color="#f4f4f4"/>
        <stop offset=".75" stop-color="#8f8f8f"/>
        <stop offset="1" stop-color="#e6e6e6"/>
      </linearGradient>
    </defs>
    <path role="img" aria-label="Dark grey brick wall texture"
          d="M0 312 C210 296 300 190 362 118 S460 36 620 26 L620 354 L0 354 Z"
          fill="url(#wallTone)"/>
    <path d="M0 280 C200 262 282 160 340 94 S440 8 590 0"
          fill="none" stroke="url(#silverBand)" stroke-width="18"/>
    <path d="M0 300 C208 284 296 180 354 110 S454 26 620 16"
          fill="none" stroke="var(--card-black)" stroke-width="8"/>
  </svg>

  <div class="brand"><span class="brand__dot"></span><span class="brand__name"><span class="brand__line">Quarlwick</span><span class="brand__line">Builders</span></span></div>

  <div class="contact">
    <p class="contact__name">Darren Holloway</p>
    <p class="contact__title">Managing Director</p>
    <p class="contact__line">021-408 733 615
      <svg class="contact__icon" viewBox="0 0 16 16"><path fill="var(--accent)" d="M3 1h3l1.5 4-2 1.5a9 9 0 0 0 4 4l1.5-2 4 1.5v3a2 2 0 0 1-2 2C6.5 15 1 9.5 1 3a2 2 0 0 1 2-2z"/></svg>
    </p>
    <p class="contact__line">info@quarlwick.com
      <svg class="contact__icon" viewBox="0 0 16 16"><rect x="1" y="3" width="14" height="10" rx="1.5" fill="var(--accent)"/><path d="M1.5 4l6.5 5 6.5-5" fill="none" stroke="var(--card-black)" stroke-width="1.4"/></svg>
    </p>
    <p class="contact__line">www.quarlwickbuilders.com
      <svg class="contact__icon" viewBox="0 0 16 16"><circle cx="8" cy="8" r="6.5" fill="none" stroke="var(--accent)" stroke-width="1.6"/><path d="M1.5 8h13M8 1.5c-3 3.5-3 9.5 0 13M8 1.5c3 3.5 3 9.5 0 13" fill="none" stroke="var(--accent)" stroke-width="1.3"/></svg>
    </p>
  </div>

  <p class="services"><span class="services__dot">•</span>PATIOS<span class="services__dot">•</span>SIDEWALKS<span class="services__dot">•</span>RETAINING WALLS<span class="services__dot">•</span>FOUNDATIONS</p>
</section>

</body>
</html>
```